Proposal Poster, posters for kids to hold

I am proposing to my girlfriend soon, I need two posters made for my kids to hold one I want to say “be my mommy”
And the other “will you marry my daddy”
Both in horizontal format. I plan on sending the files to a print shop to get them printed on a large poster. Simple is fine with maybe a few graphics. Open to anything. Kids will be holding it from the beach as we are on a jet ski close to shore. Must be readable font from a short distance

• Cute but readable font from a distance

```html
<!DOCTYPE html>
<html lang="en">
<head>
<meta charset="utf-8">
<title>Proposal Posters</title>
<link href="https://fonts.googleapis.com/css2?family=Lobster+Two:ital,wght@1,700&display=swap" rel="stylesheet">
<style>
  :root {
    --stage-dark: #7d7d7d;
    --stage-light: #d2d2d2;
    --poster-pink: #f6b8d8;
    --poster-glow: #fde6f2;
    --petal-pink: rgba(240, 140, 190, 0.75);
    --petal-clear: rgba(240, 140, 190, 0);
    --bloom-orange: rgba(244, 170, 60, 0.85);
    --bloom-clear: rgba(244, 170, 60, 0);
    --leaf-green: rgba(46, 160, 112, 0.55);
    --leaf-clear: rgba(46, 160, 112, 0);
    --ink-white: #ffffff;
    --outline-pink: #e0589e;
  }
  html, body {
    margin: 0;
    padding: 0;
    width: 1200px;
    height: 683px;
    overflow: hidden;
  }
  .stage {
    position: relative;
    width: 1200px;
    height: 683px;
    background: linear-gradient(90deg, var(--stage-dark), var(--stage-light));
  }
  .poster {
    position: absolute;
    top: 156px;
    width: 520px;
    height: 370px;
    overflow: hidden;
    background: radial-gradient(ellipse 60% 60% at 50% 50%, var(--poster-glow) 0%, var(--poster-pink) 100%);
  }
  .poster--mommy { left: 50px; }
  .poster--marry { left: 630px; }
  .flower-frame {
    position: absolute;
    inset: 0;
    background:
      radial-gradient(circle at 6% 10%, var(--bloom-orange) 0 40px, var(--petal-pink) 41px 72px, var(--petal-clear) 90px),
      radial-gradient(circle at 94% 88%, var(--bloom-orange) 0 40px, var(--petal-pink) 41px 72px, var(--petal-clear) 90px),
      radial-gradient(circle at 35% 6%, var(--bloom-orange) 0 26px, var(--bloom-clear) 46px),
      radial-gradient(circle at 78% 8%, var(--petal-pink) 0 30px, var(--petal-clear) 52px),
      radial-gradient(circle at 3% 55%, var(--bloom-orange) 0 24px, var(--bloom-clear) 44px),
      radial-gradient(circle at 97% 45%, var(--bloom-orange) 0 24px, var(--bloom-clear) 44px),
      radial-gradient(circle at 20% 94%, var(--bloom-orange) 0 26px, var(--bloom-clear) 46px),
      radial-gradient(circle at 60% 96%, var(--petal-pink) 0 30px, var(--petal-clear) 52px),
      radial-gradient(circle at 50% 0%, var(--leaf-green) 0 18px, var(--leaf-clear) 40px),
      radial-gradient(circle at 10% 82%, var(--leaf-green) 0 16px, var(--leaf-clear) 36px);
  }
  .headline {
    position: absolute;
    left: 0;
    top: 0;
    width: 100%;
    height: 100%;
    margin: 0;
    transform: rotate(-5deg);
    transform-origin: 50% 50%;
  }
  .headline span {
    position: absolute;
    display: block;
    white-space: nowrap;
    font-family: 'Lobster Two', cursive;
    font-style: italic;
    font-weight: 700;
    line-height: 1;
    color: var(--ink-white);
    -webkit-text-stroke: 8px var(--outline-pink);
    paint-order: stroke fill;
    text-shadow: 0 4px 8px rgba(160, 40, 100, 0.45);
  }
  .poster--mommy .line-be-my { left: 165px; top: 88px; font-size: 64px; }
  .poster--mommy .line-mommy { left: 95px; top: 150px; font-size: 110px; }
  .poster--marry .line-will-you { left: 140px; top: 58px; font-size: 46px; }
  .poster--marry .line-marry { left: 100px; top: 106px; font-size: 88px; }
  .poster--marry .line-daddy { left: 105px; top: 194px; font-size: 88px; }
</style>
</head>
<body>
  <main class="stage">
    <section class="poster poster--mommy">
      <div class="flower-frame" role="img" aria-label="Frame of paper-cut pink and orange flowers with green leaves around the poster edges"></div>
      <h1 class="headline">
        <span class="line-be-my">Be my</span>
        <span class="line-mommy">mommy</span>
      </h1>
    </section>
    <section class="poster poster--marry">
      <div class="flower-frame" role="img" aria-label="Frame of paper-cut pink and orange flowers with green leaves around the poster edges"></div>
      <h1 class="headline">
        <span class="line-will-you">Will you</span>
        <span class="line-marry">marry</span>
        <span class="line-daddy">My Daddy</span>
      </h1>
    </section>
  </main>
</body>
</html>
```